Pilates Classes Flyer Design

I need a flyer designed that will promote my range of classes held in Bath, UK. I teach beginners, intermediate level and Over 50's and 60's and also teach individuals in their own homes. I would like to see designs using my colours blue Pantone 306 and Lime Green 14-0452 TPX TCX. The flyer should reflect a friendly, welcoming and professional class structure. I attach an old flyer for your reference and copy.

Target Market(s)

Men and Women who have busy lives working hard, who recognise they need to stretch out, do some exercise and de-stress after a busy day

Ladies over 50 who want to do some Pilates in a friendly fun environment and meet people at the same time.

Industry/Entity Type

It Professional

Font styles to use
Sans Serif
Script

Requirements
Must have
• One-sided flyer
Text only logo. Drop the figure

```html
<!DOCTYPE html>
<html lang="en">
<head>
<meta charset="utf-8">
<title>Flow Form Pilates – New classes near you</title>
<link rel="stylesheet" href="https://fonts.googleapis.com/css2?family=Fredoka:wght@400;500;600&display=swap">
<style>
  :root {
    --lime: #a6c532;
    --sky: #5fd3ee;
    --sky-soft: #8fdcf0;
    --white: #ffffff;
    --ink: #1d2740;
    --badge-edge: #6f8a1c;
    --figure-tone: rgba(255,255,255,0.22);
  }
  * { margin: 0; padding: 0; box-sizing: border-box; }
  html, body { width: 851px; height: 1200px; overflow: hidden; background: var(--white); }
  .flyer {
    position: relative; width: 851px; height: 1200px; overflow: hidden;
    background: var(--lime);
    font-family: "Fredoka", "Arial Rounded MT Bold", sans-serif;
    color: var(--white);
  }
  .header-curve { position: absolute; left: 0; top: 0; width: 851px; height: 310px; }
  .brand {
    position: absolute; left: 300px; top: 95px;
    display: flex; align-items: center; gap: 16px;
  }
  .brand-dot { width: 22px; height: 22px; border-radius: 50%; background: var(--sky); }
  .brand-name {
    font-weight: 400; font-size: 58px; line-height: 0.95; color: var(--sky);
    letter-spacing: -0.5px;
  }
  .headline {
    position: absolute; top: 318px; width: 100%; text-align: center;
    font-weight: 600; font-size: 63px; letter-spacing: -0.3px;
  }
  .intro {
    position: absolute; top: 408px; left: 0; width: 100%; text-align: center;
    font-weight: 600; font-size: 27px; line-height: 34px;
  }
  .features {
    position: absolute; top: 527px; left: 0; width: 100%; height: 154px;
    background: var(--sky); list-style: none; padding: 17px 0 0 80px;
  }
  .features li {
    position: relative; font-weight: 500; font-size: 20.5px; line-height: 35px; color: var(--ink);
    padding-left: 26px;
  }
  .features li::before {
    content: ""; position: absolute; left: 0; top: 12px;
    width: 12px; height: 12px; border-radius: 50%; background: var(--ink);
  }
  .figure-area {
    position: absolute; left: 62px; top: 698px; width: 96px; height: 330px;
    border-radius: 48px 48px 20px 20px; background: var(--figure-tone);
  }
  .venues-title {
    position: absolute; left: 236px; top: 706px; font-weight: 500; font-size: 31px;
  }
  .venues { position: absolute; left: 182px; top: 756px; width: 628px; list-style: none; }
  .venue {
    position: relative; padding: 5px 0 9px 54px; font-weight: 500; font-size: 21px; line-height: 35px;
    border-bottom: 1.5px solid var(--white);
  }
  .venue:last-child { border-bottom: none; }
  .venue + .venue { padding-top: 8px; }
  .venue::before {
    content: ""; position: absolute; left: 20px; top: 18px;
    width: 11px; height: 11px; border-radius: 50%; background: var(--white);
  }
  .venue span { display: block; }
  .contact-band {
    position: absolute; left: 0; top: 1040px; width: 100%; height: 160px; background: var(--sky);
  }
  .contact {
    position: absolute; left: 60px; top: 30px; width: 462px; text-align: center;
    font-family: Arial, Helvetica, sans-serif; font-weight: 700; font-size: 24px; line-height: 34px;
    color: var(--ink);
  }
  .contact a { color: inherit; text-decoration: none; }
  .badge {
    position: absolute; left: 517px; top: 10px; width: 274px; height: 88px;
    background: var(--lime); border: 2px solid var(--badge-edge); border-radius: 4px;
  }
</style>
</head>
<body>
<main class="flyer">
  <svg class="header-curve" viewBox="0 0 851 310" aria-hidden="true">
    <path d="M0 0 H851 V150 C700 175 560 300 420 296 C260 292 120 180 0 170 Z" fill="#ffffff"/>
    <path d="M0 178 C120 190 260 300 420 304 C560 308 700 183 851 158" fill="none" stroke="#8fdcf0" stroke-width="3"/>
  </svg>

  <div class="brand">
    <span class="brand-dot"></span>
    <div class="brand-name">Flow<br>Form Pilates</div>
  </div>

  <h1 class="headline">New classes near you!</h1>
  <p class="intro">Pilates is for EVERYONE whatever level<br>of fitness, age or ability to help you build<br>strength, flexibility and overall well-being.</p>

  <ul class="features">
    <li>Quality teaching with Steady Balance Method Teacher.</li>
    <li>Progressive approach. Teaching good movement skills.</li>
    <li>Small class sizes and friendly atmosphere.</li>
    <li>Beginners, Intermediate and Over 50’s classes to choose from</li>
  </ul>

  <div class="figure-area" role="img" aria-label="Decorative outline of a stretching figure"></div>

  <h2 class="venues-title">Join my one-hour classes at:</h2>
  <ul class="venues">
    <li class="venue"><span>St Anne’s Church Hall,</span><span>Elm Flat</span><span>Monday evenings, Tuesday and Friday mornings.</span></li>
    <li class="venue"><span>Brookfield Dr. Surgery</span><span>Tuesday evenings.</span></li>
    <li class="venue"><span>Hartwell Centre, Mill Road,</span><span>Wednesday mornings and evenings.</span></li>
  </ul>

  <footer class="contact-band">
    <p class="contact">Call Ellen on 07700900123<br><a href="mailto:ellen.hartley@example.co.uk">ellen.hartley@example.co.uk</a></p>
    <div class="badge" role="img" aria-label="Teacher certification badge"></div>
  </footer>
</main>
</body>
</html>
```